Linked In Business banner needed

The image size is 1128 px X 191 px

This is a Linkfold Company Banner. Vantor Quell is the company and I have attached our logo. We are an advance staffing company that only recruits sales professionals.

```html
<!DOCTYPE html>
<html lang="en">
<head>
<meta charset="utf-8">
<title>Linkfold Banner for Company Profile</title>
<link href="https://fonts.googleapis.com/css2?family=Open+Sans:wght@400;700&family=Roboto+Condensed:wght@400&display=swap" rel="stylesheet">
<style>
  :root {
    --bg-blue: #3375b3;
    --white: #ffffff;
    --frame-grey: #e4e4e4;
    --bar-grey: #d3d1d1;
    --accent-yellow: #f7b928;
    --brand-ink: #333a44;
    --claim-blue: #3375b3;
    --logo-blue: #3a77b5;
  }
  * { margin: 0; padding: 0; box-sizing: border-box; }
  html, body { width: 1200px; height: 566px; overflow: hidden; }
  body {
    position: relative;
    background: var(--bg-blue);
    font-family: "Open Sans", Arial, sans-serif;
    color: var(--white);
  }
  .headline {
    position: absolute;
    left: 0; right: 0; top: 20px;
    text-align: center;
    font-weight: 700;
    line-height: 1.25;
  }
  .headline-main { font-size: 53px; display: block; margin-left: -40px; }
  .headline-sub { font-size: 42px; display: block; margin-top: 2px; margin-left: -50px; }

  .spec {
    position: absolute;
    text-align: center;
    font-weight: 700;
  }
  .spec-title { font-size: 22px; line-height: 32px; display: block; }
  .spec-size { font-size: 20px; display: block; }
  .spec-banner { left: 960px; width: 220px; top: 97px; }
  .spec-banner .spec-size { margin-top: 10px; }
  .spec-logo { left: 22px; width: 180px; top: 200px; }
  .spec-logo .spec-size { margin-top: 3px; margin-left: 14px; }

  .guides { position: absolute; left: 0; top: 0; }

  .profile-frame {
    position: absolute;
    left: 209px; top: 230px;
    width: 776px; height: 308px;
    background: var(--frame-grey);
  }
  .profile-card {
    position: absolute;
    left: 7px; top: 28px;
    width: 762px; height: 236px;
    background: var(--white);
  }
  .profile-footer {
    position: absolute;
    left: 7px; top: 271px;
    width: 762px; height: 37px;
    background: var(--white);
  }
  .cover {
    position: absolute;
    left: 0; top: 0;
    width: 762px; height: 129px;
    background: var(--white);
    border: 1px solid #e8e8e8;
    overflow: hidden;
  }
  .cover-photo {
    position: absolute;
    left: 0; top: 0;
    width: 500px; height: 129px;
    background: linear-gradient(90deg, #cfcfcf 0%, #e6e6e6 40%, #efefef 75%, rgba(255,255,255,0) 100%);
  }
  .cover-photo::after {
    content: "";
    position: absolute; left: 0; bottom: 0;
    width: 100%; height: 36px;
    background: linear-gradient(90deg, #9a9a9a 0%, #c6c6c6 60%, rgba(255,255,255,0) 100%);
  }
  .cover-brand {
    position: absolute;
    left: 470px; top: 30px;
    width: 280px;
  }
  .brand-name {
    font-family: "Open Sans", Arial, sans-serif;
    font-size: 38px; font-weight: 700;
    color: var(--brand-ink);
    line-height: 46px;
    white-space: nowrap;
  }
  .brand-claim {
    margin-top: 14px;
    font-family: "Roboto Condensed", Arial, sans-serif;
    font-size: 21px;
    color: var(--claim-blue);
    letter-spacing: 0.6px;
    white-space: nowrap;
  }
  .logo-badge {
    position: absolute;
    left: 243px; top: 302px;
    width: 121px; height: 121px;
    border-radius: 50%;
    background: var(--logo-blue);
    border: 4px solid var(--white);
    display: flex; align-items: center; justify-content: center;
    font-size: 25px; font-weight: 400;
  }
  .placeholder-line {
    position: absolute;
    height: 12px;
    background: var(--bar-grey);
  }
</style>
</head>
<body>
  <h1 class="headline">
    <span class="headline-main">Linkfold Banner for</span>
    <span class="headline-sub">Company Profile</span>
  </h1>

  <div class="spec spec-banner">
    <span class="spec-title">Company Banner</span>
    <span class="spec-title">Image Size</span>
    <span class="spec-size">1128 X 191 pixels</span>
  </div>

  <div class="spec spec-logo">
    <span class="spec-title">Logo Image Size</span>
    <span class="spec-size">300 X 300 pixels</span>
  </div>

  <div class="profile-frame">
    <div class="profile-card">
      <div class="cover">
        <div class="cover-photo" role="img" aria-label="Photo of a row of business professionals standing in line, shown from the waist down"></div>
        <div class="cover-brand">
          <div class="brand-name">Vantor Quell</div>
          <div class="brand-claim">SALES PROFESSIONALS ONLY</div>
        </div>
      </div>
    </div>
    <div class="profile-footer"></div>
  </div>

  <div class="placeholder-line" style="left:245px; top:435px; width:176px;"></div>
  <div class="placeholder-line" style="left:245px; top:453px; width:136px;"></div>
  <div class="placeholder-line" style="left:770px; top:432px; width:176px;"></div>
  <div class="placeholder-line" style="left:770px; top:450px; width:176px;"></div>
  <div class="placeholder-line" style="left:770px; top:468px; width:176px;"></div>

  <div class="logo-badge">Logo</div>

  <svg class="guides" width="1200" height="566" viewBox="0 0 1200 566" aria-hidden="true">
    <g fill="none" stroke="var(--accent-yellow)" stroke-width="4.5" stroke-dasharray="10 8">
      <polyline points="1068,257 1068,313 982,313"/>
      <polyline points="127,308 127,362 215,362"/>
    </g>
    <g fill="var(--accent-yellow)">
      <polygon points="1068,221 1083,246 1053,246"/>
      <polygon points="127,271 142,297 112,297"/>
    </g>
  </svg>
</body>
</html>
```